Stanbrook Fire Services Pty Ltd

We need business cards for a company based in Perth, we install, service and maintain fire equipment.
On the front we want a great design with our logo and a small spot for our full company name, general company email address and office number. On the back we need space for our name, title, mobile number and email address on the back.

Target Market(s)

Facility managers and commercial/industrial building owners/occupiers.

Contact Information for Business Card

Font styles to use
Sans Serif

Requirements
Must have
• Please only submit 5 of your best samples.
Darker tones are preferred.
Nice to have
• We want to use, black, red and grey. Keep it modern and clean.
I've attached the company logo and a sample of a boarder we use on our emergency plans.
Should not have
• No preference. Let the designer choose.

```html
<!DOCTYPE html>
<html lang="en">
<head>
<meta charset="utf-8">
<title>Stanbrook Fire Services – Business Cards</title>
<link rel="stylesheet" href="https://fonts.googleapis.com/css2?family=Catamaran:wght@300;400;700&display=swap">
<style>
  :root {
    --bg: #c9dcbc;
    --card-white: #ffffff;
    --card-black: #000000;
    --fire-red: #ee2530;
    --ink: #111111;
    --paper-text: #ffffff;
  }
  * { margin: 0; padding: 0; box-sizing: border-box; }
  html, body { width: 1200px; height: 1200px; overflow: hidden; }
  body {
    background: var(--bg);
    font-family: "Catamaran", sans-serif;
    position: relative;
  }
  .card {
    position: absolute;
    left: 247px;
    width: 708px;
    height: 404px;
    overflow: hidden;
  }
  .card--front { top: 148px; background: var(--card-white); color: var(--ink); }
  .card--back { top: 653px; background: var(--card-black); color: var(--paper-text); }

  /* Front brand block */
  .brand-block {
    position: absolute;
    left: 36px;
    top: 38px;
    width: 160px;
  }
  .brand-square {
    width: 96px;
    height: 96px;
    background: var(--fire-red);
    margin-bottom: 18px;
  }
  .brand-name {
    font-size: 36px;
    font-weight: 700;
    line-height: 1;
    color: var(--fire-red);
  }

  .company-name {
    position: absolute;
    left: 257px;
    top: 226px;
    font-size: 32px;
    font-weight: 700;
    line-height: 1;
    letter-spacing: 0.2px;
    white-space: nowrap;
  }
  .contact-list {
    position: absolute;
    left: 254px;
    top: 282px;
    list-style: none;
  }
  .contact-list li {
    display: flex;
    align-items: center;
    height: 28.5px;
    font-size: 23.5px;
    font-weight: 400;
    white-space: nowrap;
  }
  .contact-icon {
    width: 23px;
    height: 23px;
    margin-right: 11px;
    flex: none;
  }

  /* Back */
  .person {
    position: absolute;
    left: 54px;
    top: 58px;
  }
  .person-name {
    font-size: 35px;
    line-height: 1;
    font-weight: 300;
    white-space: nowrap;
  }
  .person-name strong { font-weight: 700; }
  .person-title {
    font-size: 25px;
    font-weight: 400;
    line-height: 1;
    margin-top: 10px;
  }
  .back-contacts {
    position: absolute;
    left: 54px;
    top: 238px;
    font-size: 26px;
    font-weight: 400;
    line-height: 1;
    white-space: nowrap;
  }
  .back-contacts p { margin-bottom: 11px; }
  .back-contacts .address { line-height: 25px; margin-top: 2px; }

  .brand-feature {
    position: absolute;
    left: 388px;
    top: 18px;
    width: 302px;
    height: 370px;
    display: flex;
    flex-direction: column;
    align-items: center;
    justify-content: space-between;
  }
  .brand-circle {
    width: 270px;
    height: 270px;
    border-radius: 50%;
    background: var(--fire-red);
  }
  .brand-mark-large {
    font-size: 62px;
    font-weight: 700;
    line-height: 0.9;
    color: var(--fire-red);
  }
</style>
</head>
<body>

<section class="card card--front" aria-label="Business card front">
  <div class="brand-block">
    <div class="brand-square"></div>
    <div class="brand-name">Stanbrook</div>
  </div>

  <h1 class="company-name">Stanbrook Fire Services Pty Ltd</h1>

  <ul class="contact-list">
    <li>
      <svg class="contact-icon" viewBox="0 0 24 24" aria-hidden="true">
        <circle cx="12" cy="12" r="12" fill="#111"/>
        <path d="M12 5 L19 11.5 H17 V18 H13.5 V14 H10.5 V18 H7 V11.5 H5 Z" fill="#fff"/>
      </svg>
      123 Street Name, Country Pincode.
    </li>
    <li>
      <svg class="contact-icon" viewBox="0 0 24 24" aria-hidden="true">
        <circle cx="12" cy="12" r="12" fill="#111"/>
        <rect x="8" y="5" width="8" height="14" rx="1.5" fill="#fff"/>
        <rect x="9.5" y="7" width="5" height="6" fill="#111"/>
      </svg>
      Ph: +000 12345678
    </li>
    <li>
      <svg class="contact-icon" viewBox="0 0 24 24" aria-hidden="true">
        <circle cx="12" cy="12" r="12" fill="#111"/>
        <rect x="6" y="8" width="12" height="8.5" fill="#fff"/>
        <path d="M6 8 L12 13 L18 8" fill="none" stroke="#111" stroke-width="1"/>
      </svg>
      email@hostname.com
    </li>
  </ul>
</section>

<section class="card card--back" aria-label="Business card back">
  <div class="person">
    <h2 class="person-name">FIRST <strong>NAME</strong></h2>
    <p class="person-title">Designation</p>
  </div>

  <div class="back-contacts">
    <p>+000 12345678</p>
    <p>email@hostname.com</p>
    <p class="address">123 Street Name, State,<br>Country Pincode.</p>
  </div>

  <div class="brand-feature">
    <div class="brand-circle"></div>
    <div class="brand-mark-large">Stanbrook</div>
  </div>
</section>

</body>
</html>
```